Presentation Folder, Business Card, Letterhead and Envelope design

We are a dental clinic that will open in August and we are looking for a professional graphic designer to create our Business Card, Presentation Folder, Letterhead, Notepad and envelopes.

The brand LumaGrin must reflect a sense of quality and sophistication, marketed for middle-class consumers.
Our preference is for quality and refined materials, where less is more.
Attached the logo

```html
<!DOCTYPE html>
<html lang="en">
<head>
<meta charset="utf-8">
<title>LumaGrin Stationery Set</title>
<link rel="stylesheet" href="https://fonts.googleapis.com/css2?family=Montserrat:wght@400;800&family=Roboto:wght@400;500&family=Roboto+Slab:wght@700&display=swap">
<style>
:root{
  --bg:#cdcdcd;
  --paper:#ffffff;
  --ink:#222222;
  --name-ink:#3d3d3f;
  --wine:#6e1014;
  --wine-deep:#4f0a0d;
  --grey:#8a8a8a;
  --grey-mid:#7c7c7c;
  --grey-light:#b9b9b9;
  --white:#ffffff;
}
*{box-sizing:border-box;margin:0;padding:0}
html,body{width:924px;height:1200px;overflow:hidden;background:var(--bg)}
body{font-family:"Roboto",Arial,sans-serif;color:var(--ink)}
.canvas{position:relative;width:924px;height:1200px;overflow:hidden;background:var(--bg)}
.piece{position:absolute;background:var(--paper);overflow:hidden;box-shadow:0 2px 6px rgba(0,0,0,.18)}
.brand-name{font-family:"Roboto",Arial,sans-serif;font-weight:500;color:var(--name-ink);white-space:nowrap;line-height:1}
.brand-name.on-dark{color:var(--white)}
.icon{width:8px;height:8px;fill:var(--wine);flex:none}
.icon.light{fill:var(--white)}

/* Plain footer bands */
.band{position:absolute;left:0;width:100%}
.band-grey{background:var(--grey-mid)}
.band-wine{background:linear-gradient(90deg,var(--wine-deep),var(--wine))}

/* Letterhead */
.letterhead{left:38px;top:44px;width:316px;height:446px}
.letterhead .brand-name{position:absolute;left:23px;top:29px;font-size:17px}
.letterhead .contacts{position:absolute;left:232px;top:28px;list-style:none;font-size:6.8px}
.letterhead .contacts li{display:flex;align-items:center;gap:6px;height:16px}
.letterhead .letter{position:absolute;left:23px;top:106px;width:271px;font-size:6.5px;line-height:10px}
.letter .recipient{font-weight:500;margin-bottom:7px}
.letter .meta{display:flex;justify-content:space-between;font-weight:500;margin-bottom:11px}
.letter p{text-align:justify;margin-bottom:10px}
.letter .signature{width:62px;height:28px;margin:4px 0 6px;background:#ececec}
.letterhead .band-grey{bottom:30px;height:5px}
.letterhead .band-wine{bottom:0;height:26px}

/* Envelope back */
.envelope-back{left:454px;top:39px;width:358px;height:156px}
.envelope-back .flap{position:absolute;left:0;top:0;width:100%;height:50px;display:block}
.envelope-back .brand-name{position:absolute;left:0;right:0;top:90px;text-align:center;font-size:22px}

/* Envelope front */
.envelope-front{left:520px;top:206px;width:359px;height:156px}
.envelope-front .brand-name{position:absolute;left:23px;top:30px;font-size:20px}
.envelope-front .band-grey{bottom:34px;height:5px}
.envelope-front .band-wine{bottom:0;height:30px}
.envelope-front .footer{position:absolute;right:12px;bottom:10px;display:flex;align-items:center;gap:6px;color:var(--white);font-size:8px;letter-spacing:.04em;line-height:10px}

/* Notepad */
.notepad{left:610px;top:385px;width:210px;height:303px;background:#eceef1}
.notepad .binding{position:absolute;left:0;top:0;width:100%;height:28px;background:linear-gradient(#f6f6f6,#dcdcdc)}
.notepad .header{position:absolute;left:0;top:28px;width:100%;height:20px;background:var(--wine);display:flex;justify-content:center;align-items:center}
.notepad .brand-name{font-size:12px}
.notepad .band-grey{bottom:22px;height:4px}
.notepad .band-wine{bottom:0;height:18px}

/* Business cards */
.card{width:155px;height:91px}
.card-front{left:124px;top:566px}
.card-back{left:302px;top:568px}
.card-front .brand-name{position:absolute;left:10px;top:21px;font-size:10px}
.card-front .divider{position:absolute;left:76px;top:12px;width:1px;height:30px;background:var(--grey)}
.card-front .person{position:absolute;left:81px;top:20px}
.person .name{font-family:"Roboto Slab",Georgia,serif;font-weight:700;font-size:6px;color:var(--wine)}
.person .role{font-size:4px;font-style:italic;color:var(--grey)}
.card .band-grey{bottom:36px;height:3px}
.card .band-wine{bottom:0;height:33px}
.card-front .contacts{position:absolute;left:94px;bottom:3px;list-style:none;color:var(--white);font-size:4px}
.card-front .contacts li{display:flex;align-items:center;gap:3px;height:9px}
.card-front .contacts .icon{width:5px;height:5px}
.card-back .brand-name{position:absolute;left:12px;top:20px;font-size:14px}
.card-back .web{position:absolute;right:8px;bottom:8px;color:var(--white);font-size:4px;letter-spacing:.08em;display:flex;align-items:center;gap:4px}
.card-back .web::before,.card-back .web::after{content:"";width:10px;height:.5px;background:var(--white)}

/* Presentation folder */
.folder{left:212px;top:710px;width:492px;height:470px;display:flex;background:none;border-radius:12px}
.folder-panel{position:relative;width:246px;height:100%;overflow:hidden}
.folder-back{background:linear-gradient(135deg,var(--wine-deep),var(--wine) 55%,#7b1f22);color:var(--white);text-align:center;border-radius:12px 0 0 12px}
.folder-back h2{font-family:"Montserrat",Arial,sans-serif;font-weight:800;font-size:20px;margin-top:120px;display:inline-block;border-bottom:1px solid var(--white);padding-bottom:2px}
.folder-back .icons{display:flex;justify-content:center;gap:12px;margin:12px 0 10px}
.folder-back .icon-ring{width:16px;height:16px;border:1px solid var(--white);border-radius:50%;display:flex;align-items:center;justify-content:center}
.folder-back .icon-ring .icon{fill:var(--white);width:8px;height:8px}
.folder-back address{font-style:normal;font-family:"Montserrat",Arial,sans-serif;font-weight:400;font-size:11px;line-height:19px}
.folder-back .name-frame{display:inline-block;margin-top:26px;border:1px solid rgba(255,255,255,.7);padding:12px 18px}
.folder-back .brand-name{font-size:20px}
.folder-front{background:var(--paper);border-radius:0 12px 12px 0}
.folder-front .brand-name{position:absolute;left:30px;top:44px;font-size:24px}
.folder-front .photo{position:absolute;left:0;top:100px;width:100%;height:300px;background:linear-gradient(160deg,#eef1f5 0%,#c9d2dd 45%,#9aa3ae 75%,#6c7179 100%)}
.folder-front .band-grey{bottom:64px;height:6px}
.folder-front .band-wine{bottom:0;height:58px}
.folder-front .web{position:absolute;left:0;right:0;bottom:22px;display:flex;justify-content:center;align-items:center;gap:10px;color:var(--white);font-family:"Montserrat",Arial,sans-serif;font-size:10px;letter-spacing:.12em;line-height:12px}
.folder-front .web::before,.folder-front .web::after{content:"";width:22px;height:1px;background:rgba(255,255,255,.8)}
</style>
</head>
<body>
<svg width="0" height="0" style="position:absolute" aria-hidden="true">
  <defs>
    <symbol id="i-pin" viewBox="0 0 10 10"><path d="M5 0a3.6 3.6 0 0 0-3.6 3.6C1.4 6.3 5 10 5 10s3.6-3.7 3.6-6.4A3.6 3.6 0 0 0 5 0zm0 5a1.4 1.4 0 1 1 0-2.8A1.4 1.4 0 0 1 5 5z"/></symbol>
    <symbol id="i-phone" viewBox="0 0 10 10"><path d="M2 .5l1.6 2-.8 1.2a6 6 0 0 0 3.5 3.5l1.2-.8 2 1.6-.9 1.5C4.6 9.5.5 5.4 .5 1.4z"/></symbol>
    <symbol id="i-globe" viewBox="0 0 10 10"><path d="M5 0a5 5 0 1 0 0 10A5 5 0 0 0 5 0zm3.9 4.4H7.2a7.6 7.6 0 0 0-.9-3.2 4 4 0 0 1 2.6 3.2zM5 1c.5.6 1 1.8 1.1 3.4H3.9C4 2.8 4.5 1.6 5 1zM3.7 1.2a7.6 7.6 0 0 0-.9 3.2H1.1a4 4 0 0 1 2.6-3.2zM1.1 5.6h1.7c.1 1.2.4 2.3.9 3.2a4 4 0 0 1-2.6-3.2zM5 9c-.5-.6-1-1.8-1.1-3.4h2.2C6 7.2 5.5 8.4 5 9zm1.3-.2c.5-.9.8-2 .9-3.2h1.7a4 4 0 0 1-2.6 3.2z"/></symbol>
    <linearGradient id="g-grey" x1="0" y1="0" x2="0" y2="1"><stop offset="0" stop-color="#9a9a9a"/><stop offset="1" stop-color="#6c6c6c"/></linearGradient>
  </defs>
</svg>

<main class="canvas">

  <section class="piece letterhead" aria-label="Letterhead">
    <div class="brand-name">LumaGrin</div>
    <ul class="contacts">
      <li><svg class="icon"><use href="#i-pin"/></svg>Address Here</li>
      <li><svg class="icon"><use href="#i-phone"/></svg>Phone no Here</li>
      <li><svg class="icon"><use href="#i-globe"/></svg>Webaddress Here</li>
    </ul>
    <div class="letter">
      <div class="recipient">Your Name Here</div>
      <div class="meta"><span>Address</span><span>Date : 22nd June, 2020</span></div>
      <p>Lorem Ipsum is simply dummy text of the printing and typesetting industry. Lorem Ipsum has been the industry's standard dummy text ever since the 1500s, when an unknown printer took a galley of type and scrambled it to make a type specimen book. It has survived not only five centuries, but also the leap into electronic typesetting.</p>
      <p>Lorem Ipsum is simply dummy text of the printing and typesetting industry. Lorem Ipsum has been the industry's standard dummy text ever since the 1500s, when an unknown printer took a galley of type and scrambled it to make a type specimen book. It has survived not only five centuries, but also the leap into electronic typesetting.</p>
      <div>Regards</div>
      <div class="signature" role="img" aria-label="Handwritten signature"></div>
      <div>Your Name Here<br>Designation Here</div>
    </div>
    <div class="band band-grey"></div>
    <div class="band band-wine"></div>
  </section>

  <section class="piece envelope-back" aria-label="Envelope back">
    <svg class="flap" viewBox="0 0 358 50" preserveAspectRatio="none" aria-hidden="true">
      <path d="M0 0 H358 L350 42 Q349 48 342 48 H16 Q9 48 8 42Z" fill="url(#g-grey)"/>
    </svg>
    <div class="brand-name">LumaGrin</div>
  </section>

  <section class="piece envelope-front" aria-label="Envelope front">
    <div class="brand-name">LumaGrin</div>
    <div class="band band-grey"></div>
    <div class="band band-wine"></div>
    <div class="footer">
      <svg class="icon light"><use href="#i-globe"/></svg>www.lumagrin.com |
      <svg class="icon light"><use href="#i-phone"/></svg>1234 567 890
    </div>
  </section>

  <section class="piece notepad" aria-label="Notepad">
    <div class="binding"></div>
    <div class="header"><span class="brand-name on-dark">LumaGrin</span></div>
    <div class="band band-grey"></div>
    <div class="band band-wine"></div>
  </section>

  <section class="piece card card-front" aria-label="Business card front">
    <div class="brand-name">LumaGrin</div>
    <div class="divider"></div>
    <div class="person"><div class="name">NAME GOES HERE</div><div class="role">Director</div></div>
    <div class="band band-grey"></div>
    <div class="band band-wine"></div>
    <ul class="contacts">
      <li><svg class="icon light"><use href="#i-pin"/></svg>Address Goes Here</li>
      <li><svg class="icon light"><use href="#i-phone"/></svg>1234 567 890</li>
      <li><svg class="icon light"><use href="#i-globe"/></svg>www.lumagrin.com</li>
    </ul>
  </section>

  <section class="piece card card-back" aria-label="Business card back">
    <div class="brand-name">LumaGrin</div>
    <div class="band band-grey"></div>
    <div class="band band-wine"></div>
    <div class="web">www.lumagrin.com</div>
  </section>

  <section class="piece folder" aria-label="Presentation folder">
    <div class="folder-panel folder-back">
      <h2>CONTACT US</h2>
      <div class="icons">
        <span class="icon-ring"><svg class="icon"><use href="#i-pin"/></svg></span>
        <span class="icon-ring"><svg class="icon"><use href="#i-phone"/></svg></span>
        <span class="icon-ring"><svg class="icon"><use href="#i-globe"/></svg></span>
      </div>
      <address>Address Goes Here<br>1234 567 890<br>www.lumagrin.com</address>
      <div class="name-frame"><span class="brand-name on-dark">LumaGrin</span></div>
    </div>
    <div class="folder-panel folder-front">
      <div class="brand-name">LumaGrin</div>
      <div class="photo" role="img" aria-label="Photo of hands with a pen reviewing documents at a desk"></div>
      <div class="band band-grey"></div>
      <div class="band band-wine"></div>
      <div class="web">www.lumagrin.com</div>
    </div>
  </section>

</main>
</body>
</html>
```